Bill board design For Marlowe’s Construction

Billboard Design Request
Please design the billboard to match the branding, colors, and overall feel of our website: Marlowe's Construction Website
MARLOWE’S CONSTRUCTION
CONCRETE BUILT FOR GENERATIONS
⭐ 5-Star Rated on Zorvix
Please Include:
* All three attached project photos
* Company logo(s)
* Phone Number: 555-214-7630
* Website: MarlowesConstruction.example
* Zorvix logo with 5-star rating graphic
* Chatterly logo
* Pixtoria logo
Service Area:
Bramley • Cedar Hollow • Fenwick • Stone Harbor
Please arrange the photos and layout in whatever way creates the strongest visual impact and readability from the road. The company name, headline, phone number, and website should be highly visible at highway speeds.
The overall appearance should be clean, professional, premium, and consistent with our website branding while highlighting our reputation, craftsmanship, and quality concrete work.
People Driving By
Concrete Construction

```html
<!DOCTYPE html>
<html lang="en">
<head>
<meta charset="utf-8">
<title>Marlowe’s Construction – Concrete Billboard</title>
<link href="https://fonts.googleapis.com/css2?family=Anton&family=Oswald:wght@500;600;700&family=Montserrat:wght@500;600&display=swap" rel="stylesheet">
<style>
  :root{
    --page:#efefef;
    --ink:#0d0d0f;
    --panel:#151517;
    --brand-blue:#1e9cf0;
    --white:#ffffff;
    --gold:#f7b51c;
    --grey:#7b7d80;
    --photo-drive-a:#8a9a6e;
    --photo-drive-b:#d8d2c6;
    --photo-crew-a:#5b4a3a;
    --photo-crew-b:#a5825e;
    --photo-path-a:#7a4a32;
    --photo-path-b:#c2744c;
  }
  html,body{margin:0;padding:0;width:1139px;height:1200px;overflow:hidden;background:var(--page);}
  .billboard{
    position:absolute;left:69px;top:350px;width:1001px;height:500px;
    box-shadow:0 10px 24px rgba(0,0,0,.35);
  }
  .billboard svg{display:block;width:1001px;height:500px;}
  .brand-name{font-family:'Montserrat',sans-serif;font-weight:600;fill:var(--brand-blue);}
  .headline{font-family:'Anton',sans-serif;fill:var(--white);}
  .tagline{font-family:'Oswald',sans-serif;font-weight:600;fill:var(--brand-blue);}
  .phone-number{font-family:'Anton',sans-serif;fill:var(--white);}
  .rating-label{font-family:'Oswald',sans-serif;font-weight:500;}
  .social-name{font-family:'Oswald',sans-serif;font-weight:500;fill:var(--white);}
  .service-area{font-family:'Oswald',sans-serif;font-weight:600;fill:var(--ink);}
  .website{font-family:'Montserrat',sans-serif;font-weight:600;fill:var(--white);}
  .website .tld{fill:var(--brand-blue);}
</style>
</head>
<body>
<div class="billboard">
<svg viewBox="0 0 1001 500" xmlns="http://www.w3.org/2000/svg">
  <defs>
    <linearGradient id="grad-drive" x1="0" y1="0" x2="0" y2="1">
      <stop offset="0" stop-color="var(--photo-drive-a)"/>
      <stop offset="1" stop-color="var(--photo-drive-b)"/>
    </linearGradient>
    <linearGradient id="grad-crew" x1="0" y1="0" x2="1" y2="1">
      <stop offset="0" stop-color="var(--photo-crew-a)"/>
      <stop offset="1" stop-color="var(--photo-crew-b)"/>
    </linearGradient>
    <linearGradient id="grad-path" x1="0" y1="0" x2="0" y2="1">
      <stop offset="0" stop-color="var(--photo-path-a)"/>
      <stop offset="1" stop-color="var(--photo-path-b)"/>
    </linearGradient>
    <linearGradient id="grad-panel" x1="0" y1="0" x2="1" y2="1">
      <stop offset="0" stop-color="#101012"/>
      <stop offset="1" stop-color="#1d1d20"/>
    </linearGradient>
  </defs>

  <!-- base panel -->
  <rect class="panel" width="1001" height="500" fill="url(#grad-panel)"/>

  <!-- project photos -->
  <polygon class="photo photo-driveway" role="img" aria-label="Project photo: new concrete driveway leading to a brick garage" points="600,0 1001,0 1001,276 517,276" fill="url(#grad-drive)"/>
  <rect class="photo-divider" x="515" y="276" width="486" height="7" fill="var(--brand-blue)"/>
  <polygon class="photo photo-crew" role="img" aria-label="Project photo: crew pouring concrete on site" points="515,283 782,283 745,435 475,435" fill="url(#grad-crew)"/>
  <polygon class="photo photo-walkway" role="img" aria-label="Project photo: stamped colored concrete walkway" points="785,283 1001,283 1001,435 748,435" fill="url(#grad-path)"/>

  <!-- blue diagonal accent -->
  <polygon class="accent-stripe" points="594,0 603,0 480,435 471,435" fill="var(--brand-blue)"/>

  <!-- brand -->
  <g class="brand">
    <rect x="31" y="40" width="30" height="30" fill="var(--brand-blue)"/>
    <text class="brand-name" x="76" y="66" font-size="38">MARLOWE’S</text>
    <text class="brand-name" x="78" y="96" font-size="17" letter-spacing="5">CONSTRUCTION L.L.C</text>
  </g>

  <!-- headline -->
  <text class="headline" x="28" y="222" font-size="96" textLength="440" lengthAdjust="spacingAndGlyphs">CONCRETE</text>
  <g class="tagline-row">
    <rect x="29" y="244" width="41" height="2" fill="var(--brand-blue)"/>
    <text class="tagline" x="248" y="258" font-size="30" text-anchor="middle" letter-spacing="2.5">BUILT FOR GENERATIONS</text>
    <rect x="427" y="244" width="42" height="2" fill="var(--brand-blue)"/>
  </g>

  <!-- phone band -->
  <polygon class="phone-band" points="0,275 513,275 494,345 0,345" fill="var(--brand-blue)"/>
  <g class="phone-icon">
    <rect x="33" y="285" width="49" height="49" rx="5" fill="none" stroke="var(--white)" stroke-width="2.5"/>
    <path d="M47 296 c-3 2 -4 5 -2 10 c3 8 9 14 17 18 c5 2 8 1 10 -2 l-5 -5 c-2 1 -4 2 -6 1 c-4 -2 -7 -5 -9 -9 c-1 -2 0 -4 1 -6 z" fill="var(--white)"/>
  </g>
  <text class="phone-number" x="102" y="336" font-size="56" textLength="334" lengthAdjust="spacingAndGlyphs">555-214-7630</text>

  <!-- rating & social -->
  <g class="rating">
    <circle cx="38" cy="392" r="19" fill="var(--white)"/>
    <text class="rating-label" x="65" y="389" font-size="17" fill="var(--gold)">5-STAR RATED</text>
    <text class="rating-label" x="73" y="409" font-size="17" fill="var(--white)">ON ZORVIX</text>
    <g fill="var(--gold)">
      <path d="M206 380 l3.6 7.4 8.2 1.2 -5.9 5.7 1.4 8.1 -7.3 -3.9 -7.3 3.9 1.4 -8.1 -5.9 -5.7 8.2 -1.2z"/>
      <path d="M230 380 l3.6 7.4 8.2 1.2 -5.9 5.7 1.4 8.1 -7.3 -3.9 -7.3 3.9 1.4 -8.1 -5.9 -5.7 8.2 -1.2z"/>
      <path d="M254 380 l3.6 7.4 8.2 1.2 -5.9 5.7 1.4 8.1 -7.3 -3.9 -7.3 3.9 1.4 -8.1 -5.9 -5.7 8.2 -1.2z"/>
      <path d="M278 380 l3.6 7.4 8.2 1.2 -5.9 5.7 1.4 8.1 -7.3 -3.9 -7.3 3.9 1.4 -8.1 -5.9 -5.7 8.2 -1.2z"/>
      <path d="M302 380 l3.6 7.4 8.2 1.2 -5.9 5.7 1.4 8.1 -7.3 -3.9 -7.3 3.9 1.4 -8.1 -5.9 -5.7 8.2 -1.2z"/>
    </g>
    <rect x="325" y="372" width="2" height="42" fill="var(--brand-blue)"/>
  </g>
  <g class="social">
    <circle cx="345" cy="383" r="7" fill="var(--brand-blue)"/>
    <text class="social-name" x="356" y="389" font-size="15">Chatterly</text>
    <circle cx="345" cy="405" r="7" fill="var(--brand-blue)"/>
    <text class="social-name" x="356" y="411" font-size="15">Pixtoria</text>
  </g>

  <!-- service area band -->
  <rect x="0" y="435" width="1001" height="4" fill="var(--white)"/>
  <polygon class="service-band" points="0,439 656,439 643,500 0,500" fill="var(--brand-blue)"/>
  <g class="pin-icon" fill="var(--white)">
    <path d="M38 450 a15 15 0 0 1 15 15 c0 11 -15 25 -15 25 s-15 -14 -15 -25 a15 15 0 0 1 15 -15z"/>
    <circle cx="38" cy="465" r="5.5" fill="var(--brand-blue)"/>
  </g>
  <text class="service-area" x="71" y="480" font-size="24" textLength="558" lengthAdjust="spacing">BRAMLEY | CEDAR HOLLOW | FENWICK | STONE HARBOR</text>

  <!-- website -->
  <polygon class="web-band" points="656,439 1001,439 1001,500 643,500" fill="var(--ink)"/>
  <g class="globe-icon" fill="none" stroke="var(--brand-blue)" stroke-width="1.6">
    <circle cx="680" cy="470" r="9"/>
    <ellipse cx="680" cy="470" rx="4" ry="9"/>
    <line x1="671" y1="470" x2="689" y2="470"/>
    <line x1="673" y1="465" x2="687" y2="465"/>
    <line x1="673" y1="475" x2="687" y2="475"/>
  </g>
  <text class="website" x="699" y="477" font-size="18.5" textLength="288" lengthAdjust="spacingAndGlyphs">MarlowesConstruction<tspan class="tld">.example</tspan></text>
</svg>
</div>
</body>
</html>
```